Construction Company Website Design

I need a Website Design for a Construction Company. I have attached logo and business card design files (a.i) to match styles and text for the website. I will need design for 3 pages:
1. A Home page
2. A secondary page (will be different information pages)
3. A contact page with submision form
Website to look professional and match the 'theme' across all pages, using main colours / reverse colours as per design files. Must be clear it is a construction related website without being over the top. Happy for the construction related details (whether that be images/outlines/backgrounds etc to be fairly subtle and not overbearing on the contect of the pages. It will be the content that will be most important, not the images within.

Content has not yet been fully completed but attached is a site map. Each page will need a space for the insertion of the relevant heading and associated content for that particular page. Example can be used as per attached map. If it is preferable to have content completed for this to be a more succesful project please advise and I will complete and submit.

Target Market(s)

Clients for potential construction projects. These could be a range of people. All would be very professional, well educated and put a substantial expection on the quality of website provided.

Industry/Entity Type

Construction

Number of Pages Required

3 page

Font styles to use
Serif
Sans Serif
Other font styles liked:
• fonts preferable as per design files provided unless designer beleives a different font would suit better

Requirements
Must have
• Colour scheme to match logo and business card files provided. Fonts that match as per provided files. Pages must be consistent with the theme carrying across all pages. All pages must have contact details at the bottom of the page.
• Contents of page 1 - 'Home page': multiple tab options / logo link
• Contents of page 2 - 'Secondary page': Top and side navigation / area for information and/or images.
• Contents of page - 'Contact us page': Top and side navigation / Submission form / area for logos such as linkdin, facebook etc.
Nice to have
• Would be good to have a or some generic construction related images - outlines / shadows / effects etc. These might be background images or outlines related to the relevant industry and are consistent across the pages. Could be outlines of buildings, images of men with hardhats etc etc. Good to see colour scheme as per design files used
Should not have
• No pictures of houses. Generally no photos. If any imagery of people must not show faces/details.

```html
<!DOCTYPE html>
<html lang="en">
<head>
<meta charset="utf-8">
<title>K.R.M Constructions</title>
<link href="https://fonts.googleapis.com/css2?family=Ubuntu:wght@400;500&family=Arimo:wght@400;700&family=Open+Sans:wght@400;600;700&display=swap" rel="stylesheet">
<style>
:root{
  --blue:#12a3e3;
  --blue-dark:#0a86c4;
  --ink:#333a40;
  --text:#4b4f54;
  --muted:#8a8f94;
  --grey-band:#eeeeee;
  --white:#ffffff;
  --line:#c9cdd1;
  --tile-dark:#4a4f55;
}
*{margin:0;padding:0;box-sizing:border-box}
html,body{width:1200px;height:4712px;overflow:hidden}
body{position:relative;background:var(--white);font-family:"Arimo",Arial,sans-serif;color:var(--text)}
.abs{position:absolute}
a{color:inherit;text-decoration:none}

/* header */
.site-header{position:absolute;left:0;top:0;width:1200px;height:95px;z-index:3;display:flex;align-items:center;background:linear-gradient(rgba(255,255,255,.85),rgba(255,255,255,.55))}
.brand{position:absolute;left:78px;top:30px;display:flex;align-items:center;gap:14px;font-family:"Open Sans",sans-serif;font-weight:600;font-size:21px;letter-spacing:3px;color:var(--ink)}
.brand-mark{width:14px;height:14px;background:var(--ink)}
.main-nav{position:absolute;right:60px;top:36px;display:flex;gap:43px;font-family:"Open Sans",sans-serif;font-size:16px;color:var(--ink)}
.main-nav .active{color:var(--blue)}

/* hero */
.hero{left:0;top:0;width:1200px;height:732px;background:linear-gradient(180deg,#9fb8c8 0%,#6f8797 35%,#566a78 65%,#8a9aa3 100%)}
.hero-panel{left:226px;top:276px;width:748px;height:227px;background:rgba(255,255,255,.5);text-align:center;padding-top:60px}
.hero-name{font-family:"Open Sans",sans-serif;font-weight:600;font-size:42px;letter-spacing:5px;color:var(--ink)}
.hero-tag{margin-top:16px;font-family:"Open Sans",sans-serif;font-weight:600;font-size:27px;color:var(--ink)}
.hero-btn{left:508px;top:521px;width:184px;height:48px;background:var(--blue);color:var(--white);font-family:"Open Sans",sans-serif;font-weight:700;font-size:19px;display:flex;align-items:center;justify-content:center;letter-spacing:.5px}
.hero-arrow{top:394px;width:40px;height:30px;background:var(--blue);opacity:.85}

/* section headings */
.section-title{left:0;width:1200px;text-align:center;font-family:"Ubuntu",sans-serif;font-size:45px;color:var(--ink)}
.section-title span{color:var(--blue)}
.divider{left:510px;width:180px;height:22px}
.btn{background:var(--blue);color:var(--white);font-family:"Open Sans",sans-serif;font-weight:700;display:flex;align-items:center;justify-content:center}
.lead{left:200px;width:800px;text-align:center;font-size:15.5px;line-height:29px;color:var(--text)}

/* services */
.services-head{left:0;top:1137px;width:1200px;height:230px;background:var(--grey-band)}
.service-tile{width:600px;height:401px;color:var(--white);text-align:center}
.tile-blue{background:linear-gradient(135deg,#1e9fdc,#59bde9)}
.tile-dark{background:linear-gradient(135deg,#3f454b,#6a7077)}
.tile-icon{position:absolute;left:246px;top:52px;width:108px;height:108px;border:2px solid var(--white);border-radius:50%}
.tile-icon svg{position:absolute;left:29px;top:29px}
.tile-title{position:absolute;left:0;top:175px;width:600px;font-size:22px}
.tile-text{position:absolute;left:100px;top:212px;width:400px;font-size:15px;line-height:21px}
.tile-btn{position:absolute;left:246px;top:300px;width:154px;height:40px;background:var(--white);color:var(--muted);font-size:14px;display:flex;align-items:center;justify-content:center}

/* projects */
.project-slide{top:2340px;width:400px;height:421px}
.slider-arrow{top:2531px;width:46px;height:46px;border-radius:50%;background:var(--white)}

/* culture */
.culture-band{left:0;top:2947px;width:1200px;height:336px;background:linear-gradient(120deg,#0f94d6,#39afe6 55%,#1b9bdc)}
.culture-text{left:290px;top:3000px;width:620px;text-align:center;color:var(--white);font-size:15.5px;line-height:23px}

/* news */
.news-card{top:3449px;width:418px;height:468px;border:1px solid #dcdfe2;background:var(--white)}
.news-photo{position:absolute;left:0;top:0;width:416px;height:267px}
.news-date{position:absolute;left:0;top:200px;width:56px;height:67px;background:var(--blue);color:var(--white);text-align:center;padding-top:6px}
.news-date b{display:block;font-size:28px;font-weight:400;line-height:32px}
.news-date small{font-size:13px}
.news-title{position:absolute;left:14px;top:290px;font-size:22px;color:var(--blue)}
.news-text{position:absolute;left:14px;top:330px;width:360px;font-size:15px;line-height:24px}
.news-more{position:absolute;left:14px;top:413px;font-size:13px;color:var(--blue-dark);text-decoration:underline;font-weight:700}

/* contact */
.contact-band{left:0;top:3980px;width:1200px;height:522px;background:var(--grey-band)}
.field{height:50px;background:var(--white);border:1px solid #d6d9dc;font-size:14px;color:var(--text);padding:13px 14px}
.submit{left:88px;top:4389px;width:657px;height:50px;font-size:20px}
.contact-line{left:779px;display:flex;gap:22px;font-size:15.5px;line-height:24px;color:var(--text)}

/* footer */
.site-footer{left:0;top:4502px;width:1200px;height:210px;background:var(--blue);color:var(--white)}
.footer-nav{position:absolute;left:0;top:46px;width:1200px;display:flex;justify-content:center;gap:40px;font-size:15px}
.socials{position:absolute;left:500px;top:92px;display:flex;gap:12px}
.social{width:42px;height:42px;border:2px solid var(--white);border-radius:50%}
.social.filled{background:var(--white)}
.footer-rule{position:absolute;left:78px;top:150px;width:1044px;height:1px;background:rgba(255,255,255,.7)}
.copyright{position:absolute;left:0;top:168px;width:1200px;text-align:center;font-size:15px}
</style>
</head>
<body>

<!-- Hero -->
<div class="abs hero" role="img" aria-label="Aerial photo of a city skyline with high-rise towers"></div>
<header class="site-header">
  <div class="brand"><span class="brand-mark"></span>K.R.M CONSTRUCTIONS</div>
  <nav class="main-nav">
    <a class="active">Home</a><a>About Us</a><a>Service</a><a>Projects</a><a>Culture</a><a>News</a><a>Contact Us</a>
  </nav>
</header>
<div class="abs hero-arrow" style="left:18px"></div>
<div class="abs hero-arrow" style="left:1142px"></div>
<div class="abs hero-panel">
  <div class="hero-name">K.R.M CONSTRUCTIONS</div>
  <div class="hero-tag">EXCELLENCE IN CONSTRUCTION</div>
</div>
<div class="abs btn hero-btn">CONTACT US</div>

<!-- Welcome -->
<h1 class="abs section-title" style="top:790px;font-size:44px;font-weight:400"><span>Welcome to</span> K.R.M Constructions</h1>
<p class="abs lead" style="top:893px">Lorem Ipsum is simply dummy text of the printing and typesetting industry. Lorem Ipsum has been the industry's standard dummy text ever since the 1500s, when an unknown printer took a galley of type and scrambled it to make a type specimen book. It has survived not only five centuries, but also the leap into electronic typesetting, remaining essentially unchanged.</p>
<div class="abs btn" style="left:505px;top:1024px;width:190px;height:50px;font-size:19px">READ MORE</div>

<!-- Services -->
<div class="abs services-head"></div>
<h2 class="abs section-title" style="top:1186px;font-weight:400"><span>Our</span> Services</h2>
<svg class="abs divider" style="top:1247px" viewBox="0 0 180 22"><line x1="0" y1="16" x2="72" y2="16" stroke="#aab0b5" stroke-width="2"/><line x1="108" y1="16" x2="180" y2="16" stroke="#aab0b5" stroke-width="2"/><path d="M78 18 Q90 2 102 18 Z" fill="#12a3e3"/><rect x="74" y="18" width="32" height="3" fill="#12a3e3"/></svg>
<p class="abs lead" style="top:1281px;font-size:15px;line-height:26px">Lorem Ipsum is simply dummy text of the printing and typesetting industry.<br>Lorem Ipsum has been the industry's</p>

<div class="abs service-tile tile-blue" style="left:0;top:1367px" role="img" aria-label="Commercial building construction photo tinted blue">
  <div class="tile-icon"><svg width="50" height="50" viewBox="0 0 50 50" fill="none" stroke="#fff" stroke-width="2"><rect x="10" y="8" width="18" height="36"/><rect x="28" y="18" width="12" height="26"/><path d="M15 15h8M15 22h8M15 29h8M15 36h8"/></svg></div>
  <div class="tile-title">Commercial</div>
  <div class="tile-text">Lorem Ipsum is simply dummy text of the printing and typesetting industry. Lorem Ipsum has been the industry's standard dummy text ever since the 1500s.</div>
  <div class="tile-btn">READ MORE</div>
</div>
<div class="abs service-tile tile-dark" style="left:600px;top:1367px" role="img" aria-label="Residential construction site photo in grey tones">
  <div class="tile-icon"><svg width="50" height="50" viewBox="0 0 50 50" fill="none" stroke="#fff" stroke-width="2"><path d="M5 24 L25 6 L45 24"/><path d="M11 20v24h28V20"/><rect x="20" y="30" width="10" height="14"/></svg></div>
  <div class="tile-title">Residential</div>
  <div class="tile-text">Lorem Ipsum is simply dummy text of the printing and typesetting industry. Lorem Ipsum has been the industry's standard dummy text ever since the 1500s.</div>
  <div class="tile-btn">READ MORE</div>
</div>
<div class="abs service-tile tile-dark" style="left:0;top:1768px" role="img" aria-label="City waterfront skyline photo in grey tones">
  <div class="tile-icon"><svg width="50" height="50" viewBox="0 0 50 50" fill="none" stroke="#fff" stroke-width="2"><path d="M6 26 L22 12 L38 26"/><path d="M11 22v20h22V22"/><circle cx="38" cy="36" r="7"/></svg></div>
  <div class="tile-title">Building Maintenance</div>
  <div class="tile-text">Lorem Ipsum is simply dummy text of the printing and typesetting industry. Lorem Ipsum has been the industry's standard dummy text ever since the 1500s.</div>
  <div class="tile-btn">READ MORE</div>
</div>
<div class="abs service-tile tile-blue" style="left:600px;top:1768px" role="img" aria-label="Project planning desk photo tinted blue">
  <div class="tile-icon"><svg width="50" height="50" viewBox="0 0 50 50" fill="none" stroke="#fff" stroke-width="2"><rect x="9" y="8" width="26" height="34" rx="2"/><path d="M15 18h14M15 25h10M15 32h8"/><circle cx="36" cy="36" r="8"/><path d="M36 31v5h4"/></svg></div>
  <div class="tile-title">Project Management</div>
  <div class="tile-text">Lorem Ipsum is simply dummy text of the printing and typesetting industry. Lorem Ipsum has been the industry's standard dummy text ever since the 1500s.</div>
  <div class="tile-btn">READ MORE</div>
</div>

<!-- Projects -->
<h2 class="abs section-title" style="top:2222px;font-weight:400"><span>Our</span> Projects</h2>
<svg class="abs divider" style="top:2283px" viewBox="0 0 180 22"><line x1="0" y1="16" x2="72" y2="16" stroke="#aab0b5" stroke-width="2"/><line x1="108" y1="16" x2="180" y2="16" stroke="#aab0b5" stroke-width="2"/><path d="M78 18 Q90 2 102 18 Z" fill="#12a3e3"/><rect x="74" y="18" width="32" height="3" fill="#12a3e3"/></svg>
<div class="abs project-slide" style="left:0;background:linear-gradient(180deg,#c9ccc9,#8f8e88 60%,#5e5d57)" role="img" aria-label="Concrete building frame under construction"></div>
<div class="abs project-slide" style="left:400px;background:linear-gradient(160deg,#d8ecf8,#5d9dd0 45%,#1d4e8c)" role="img" aria-label="Glass office towers viewed from below"></div>
<div class="abs project-slide" style="left:800px;background:linear-gradient(180deg,#2c3e6b,#6f7f98 45%,#a8a49a)" role="img" aria-label="Office building against a blue sky"></div>
<div class="abs slider-arrow" style="left:373px"><svg width="46" height="46" viewBox="0 0 46 46"><path d="M27 15 L19 23 L27 31" fill="none" stroke="#12a3e3" stroke-width="4"/></svg></div>
<div class="abs slider-arrow" style="left:778px"><svg width="46" height="46" viewBox="0 0 46 46"><path d="M19 15 L27 23 L19 31" fill="none" stroke="#12a3e3" stroke-width="4"/></svg></div>

<!-- Culture -->
<h2 class="abs section-title" style="top:2813px;font-weight:400">Culture</h2>
<svg class="abs divider" style="top:2874px" viewBox="0 0 180 22"><line x1="0" y1="16" x2="72" y2="16" stroke="#aab0b5" stroke-width="2"/><line x1="108" y1="16" x2="180" y2="16" stroke="#aab0b5" stroke-width="2"/><path d="M78 18 Q90 2 102 18 Z" fill="#12a3e3"/><rect x="74" y="18" width="32" height="3" fill="#12a3e3"/></svg>
<div class="abs culture-band" role="img" aria-label="Construction team at work, tinted blue"></div>
<p class="abs culture-text">Lorem Ipsum is simply dummy text of the printing and typesetting industry. Lorem Ipsum has been the industry's standard dummy text ever since the 1500s, when an unknown printer took a galley of type and scrambled it to make a type specimen book. It has survived not only five centuries, but also the leap into electronic typesetting, remaining essentially unchanged. It was popularised in the 1960s</p>
<div class="abs btn" style="left:505px;top:3161px;width:190px;height:52px;background:#fff;color:#12a3e3;font-size:19px">READ MORE</div>

<!-- News -->
<h2 class="abs section-title" style="top:3334px;font-weight:400"><span>Latest</span> News</h2>
<svg class="abs divider" style="top:3395px" viewBox="0 0 180 22"><line x1="0" y1="16" x2="72" y2="16" stroke="#aab0b5" stroke-width="2"/><line x1="108" y1="16" x2="180" y2="16" stroke="#aab0b5" stroke-width="2"/><path d="M78 18 Q90 2 102 18 Z" fill="#12a3e3"/><rect x="74" y="18" width="32" height="3" fill="#12a3e3"/></svg>
<article class="abs news-card" style="left:119px">
  <div class="news-photo" style="background:linear-gradient(160deg,#2f4c7a,#8a7f7a 50%,#e0b07a)" role="img" aria-label="Cranes over a building site at sunset"></div>
  <div class="news-date"><b>20</b><small>Apr</small></div>
  <h3 class="news-title" style="font-weight:400">Lorem Ipsum is simply dummy</h3>
  <p class="news-text">Lorem Ipsum is simply dummy text of the printing and typesetting industry. Lorem Ipsum has been the industry's</p>
  <a class="news-more">READ MORE</a>
</article>
<article class="abs news-card" style="left:663px">
  <div class="news-photo" style="background:linear-gradient(170deg,#3a6fb0,#7fa7cf 45%,#e3b26a 80%,#7a5a3a)" role="img" aria-label="Tower crane beside a rising building at dusk"></div>
  <div class="news-date"><b>20</b><small>Apr</small></div>
  <h3 class="news-title" style="font-weight:400">Lorem Ipsum is simply dummy</h3>
  <p class="news-text">Lorem Ipsum is simply dummy text of the printing and typesetting industry. Lorem Ipsum has been the industry's</p>
  <a class="news-more">READ MORE</a>
</article>

<!-- Contact -->
<div class="abs contact-band"></div>
<h2 class="abs section-title" style="top:4032px;font-weight:400"><span>Contact</span> Us</h2>
<svg class="abs divider" style="top:4093px" viewBox="0 0 180 22"><line x1="0" y1="16" x2="72" y2="16" stroke="#aab0b5" stroke-width="2"/><line x1="108" y1="16" x2="180" y2="16" stroke="#aab0b5" stroke-width="2"/><path d="M78 18 Q90 2 102 18 Z" fill="#12a3e3"/><rect x="74" y="18" width="32" height="3" fill="#12a3e3"/></svg>
<div class="abs field" style="left:88px;top:4147px;width:324px">Name</div>
<div class="abs field" style="left:421px;top:4147px;width:324px">E-mail</div>
<div class="abs field" style="left:88px;top:4213px;width:324px">Phone</div>
<div class="abs field" style="left:421px;top:4213px;width:324px">Subject</div>
<div class="abs field" style="left:88px;top:4272px;width:657px;height:104px">Message</div>
<div class="abs btn submit">SUBMIT</div>

<div class="abs contact-line" style="top:4216px">
  <svg width="16" height="22" viewBox="0 0 16 22"><path d="M8 1a7 7 0 0 1 7 7c0 5-7 13-7 13S1 13 1 8a7 7 0 0 1 7-7z" fill="#12a3e3"/><circle cx="8" cy="8" r="2.5" fill="#eee"/></svg>
  <span>111,Lorem Ipsum is simply<br>dummy text of the print.</span>
</div>
<div class="abs contact-line" style="top:4279px">
  <svg width="16" height="18" viewBox="0 0 16 18"><path d="M3 1l3 4-2 2c1 3 3 5 6 6l2-2 3 3-2 3C7 17 0 10 1 3z" fill="#12a3e3"/></svg>
  <span>020 5550 148</span>
</div>
<div class="abs contact-line" style="top:4316px">
  <svg width="18" height="14" viewBox="0 0 18 14"><rect x="1" y="1" width="16" height="12" fill="none" stroke="#12a3e3" stroke-width="1.6"/><path d="M1 1l8 7 8-7" fill="none" stroke="#12a3e3" stroke-width="1.6"/></svg>
  <span>info@krmbuild.example</span>
</div>

<!-- Footer -->
<footer class="abs site-footer">
  <nav class="footer-nav"><a>Home</a><a>About Us</a><a>Service</a><a>Projects</a><a>Culture</a><a>News</a><a>Contact Us</a></nav>
  <div class="socials"><span class="social filled"></span><span class="social"></span><span class="social"></span><span class="social"></span></div>
  <div class="footer-rule"></div>
  <p class="copyright">©KRM Construction - 2018. All Rights Reserved.</p>
</footer>

</body>
</html>
```